Flyer Designer for a Widow and Door Company - loooking for fresh design

We are looking for a flyer designed to advertise our business - we supply and install windows and doors - we are looking for a fresh looking flyer to distribute to drum up business - more information can be found at our website www.brightpanehouse.co.uk - We want a different approach than we currently have - making it vibrant and fresh - you can see the services on the website but its more the graphical design that we are looking for rather than content as the content from the website can be used for each service etc.

Target Market(s)

the general public

Colors

Designer to choose colors to be used in the design.

Requirements
Must have
• vibrant design and images

```html
<!DOCTYPE html>
<html lang="en">
<head>
<meta charset="utf-8">
<title>Brightpane House – Brochure Spread</title>
<link href="https://fonts.googleapis.com/css2?family=Quicksand:wght@400;500;700&display=swap" rel="stylesheet">
<style>
  :root{
    --bg:#dcdcdc;
    --paper:#f4f4f4;
    --orange:#e98d25;
    --blue:#4a7fc1;
    --slate:#6a6a6a;
    --ink:#5e5e5e;
    --heading:#3c3c3c;
    --photo-warm:#b9a595;
    --photo-cool:#a9b6c2;
  }
  *{box-sizing:border-box;margin:0;padding:0}
  html,body{width:1200px;height:1200px;overflow:hidden;background:var(--bg);font-family:"Quicksand",sans-serif;color:var(--ink)}
  .spread{position:absolute;left:40px;top:200px;width:1120px;height:800px;display:flex;box-shadow:0 12px 30px rgba(0,0,0,.18)}
  .page{position:relative;width:560px;height:800px;background:var(--paper);overflow:hidden}
  .page--left{border-right:1px solid #d6d6d6}

  .intro{position:absolute;left:40px;top:34px;width:480px;font-size:12px;line-height:1.5;letter-spacing:.3px}
  .intro::before{content:"";display:inline-block;width:8px;height:8px;background:var(--orange);margin-right:8px}

  .photo{position:absolute}
  .photo--strip{left:0;top:170px;width:560px;height:150px;background:linear-gradient(90deg,#d9d9d6 0%,#b48a72 35%,#c9c9c6 60%,#9a9a9a 100%)}
  .photo--hero{left:0;top:30px;width:560px;height:360px;background:linear-gradient(100deg,#a58777 0%,#8f8f8f 30%,var(--photo-cool) 60%,#d1d8de 100%)}
  .stripe{position:absolute;top:0;height:100%;opacity:.85}
  .stripe--blue{background:var(--blue)}
  .stripe--orange{background:var(--orange)}

  .service{position:absolute;width:230px}
  .service h3{font-size:13px;font-weight:700;letter-spacing:1.5px;text-transform:uppercase;color:var(--heading);line-height:1.15}
  .service p{font-size:10.5px;line-height:1.4;margin-top:3px;letter-spacing:.4px}

  .ring{position:absolute;left:0;top:0}

  .solutions{position:absolute;left:0;top:610px;width:270px;height:120px;background:var(--slate);color:#e8e8e8;padding:16px 18px}
  .solutions h2{font-size:14px;font-weight:700;letter-spacing:1.5px;text-transform:uppercase;line-height:1.15;color:#fff}
  .solutions p{font-size:10.5px;line-height:1.45;margin-top:6px}
  .site{position:absolute;left:22px;bottom:28px;font-size:13px;letter-spacing:1px;color:#bdbdbd}

  .block{position:absolute;left:36px;width:500px}
  .block__head{display:flex;align-items:center;gap:8px}
  .block__head svg{flex:none}
  .block h3{font-size:13px;font-weight:700;letter-spacing:1.5px;text-transform:uppercase;color:var(--heading);line-height:1.1}
  .block p{font-size:10.5px;line-height:1.45;margin-top:4px;letter-spacing:.2px}
  .block .list{color:var(--blue);font-size:10.5px;margin-top:3px}
  .block .list::before{content:"";display:inline-block;width:6px;height:6px;background:var(--orange);margin-right:5px}

  .footer{position:absolute;left:0;right:0;bottom:0;height:44px;display:flex;align-items:center;justify-content:flex-end;gap:16px;padding-right:24px;background:#e6e6e6}
  .phone{display:flex;align-items:center;gap:8px;font-size:15px;letter-spacing:1.5px;color:#8a8a8a}
  .brand{display:flex;align-items:center;gap:6px;font-size:13px;font-weight:700;color:#8a8a8a;letter-spacing:.5px}
  .brand__mark{width:10px;height:10px;background:var(--blue)}
</style>
</head>
<body>
<div class="spread">
  <section class="page page--left">
    <p class="intro">The Brightpane House team have many years' experience supplying and fitting the highest quality windows and doors throughout Wessex. Our experienced, friendly team are able to offer a personal touch to your project ensuring you are fully informed at all times and completely happy with the product choices you have made. Our installers will ensure that your installation is carried out to the highest standards, meeting all current regulations and making sure your home is left spotless upon completion.</p>

    <div class="photo photo--strip" role="img" aria-label="White timber French doors set in a red brick wall beside an open top-hung window">
      <span class="stripe stripe--blue" style="left:430px;width:16px"></span>
      <span class="stripe stripe--orange" style="left:500px;width:16px"></span>
    </div>

    <div class="service" style="left:34px;top:335px">
      <h3>Window Sales<br>&amp; Installation</h3>
      <p>Our windows are individually designed to suit your home.</p>
    </div>
    <div class="service" style="left:34px;top:405px">
      <h3>Door Sales<br>&amp; Installation</h3>
      <p>A new door from Brightpane House can transform the look of your home.</p>
    </div>
    <div class="service" style="left:34px;top:475px">
      <h3>Repairs &amp;<br>Maintenance</h3>
      <p>At Brightpane House we offer a full repair and replacement service on glass units, windows and doors.</p>
    </div>

    <svg class="ring" width="560" height="800" viewBox="0 0 560 800" aria-hidden="true">
      <g fill="none" stroke-width="1.2">
        <polyline points="250,352 330,352 390,395" stroke="var(--orange)"/>
        <polyline points="235,422 300,422 300,480 430,520" stroke="var(--blue)"/>
        <polyline points="215,492 280,492 280,600 420,630" stroke="var(--blue)"/>
      </g>
      <circle cx="250" cy="352" r="4" fill="var(--orange)"/>
      <circle cx="235" cy="422" r="4" fill="var(--blue)"/>
      <circle cx="215" cy="492" r="4" fill="var(--blue)"/>

      <g fill="none" stroke-width="90">
        <circle cx="340" cy="560" r="165" stroke="var(--orange)" stroke-dasharray="126.7 1036.7" transform="rotate(-100 340 560)"/>
        <circle cx="340" cy="560" r="165" stroke="var(--blue)" stroke-dasharray="126.7 1036.7" transform="rotate(-51 340 560)"/>
        <circle cx="340" cy="560" r="165" stroke="var(--blue)" stroke-dasharray="126.7 1036.7" transform="rotate(-2 340 560)"/>
        <circle cx="340" cy="560" r="165" stroke="var(--orange)" stroke-dasharray="126.7 1036.7" transform="rotate(47 340 560)"/>
      </g>

      <g fill="none" stroke="#fff" stroke-width="1.6">
        <g transform="translate(374 399)">
          <rect x="-14" y="-12" width="28" height="24"/><line x1="0" y1="-12" x2="0" y2="12"/><line x1="-14" y1="-4" x2="14" y2="-4"/>
        </g>
        <g transform="translate(484 480)">
          <rect x="-9" y="-14" width="18" height="28"/><circle cx="5" cy="1" r="1.5"/><rect x="9" y="-2" width="6" height="6"/>
        </g>
        <g transform="translate(495 616)">
          <line x1="-12" y1="10" x2="8" y2="-10"/><circle cx="10" cy="-12" r="4"/><line x1="-10" y1="-10" x2="12" y2="12"/><rect x="-14" y="-14" width="8" height="5"/>
        </g>
      </g>
    </svg>

    <div class="solutions">
      <h2>Our<br>Solutions</h2>
      <p>Offering a friendly, customer focused approach to your replacement windows and doors. Providing a full range of uPVc and aluminium to compliment your home.</p>
    </div>
    <div class="site">www.brightpanehouse.co.uk</div>
  </section>

  <section class="page page--right">
    <div class="photo photo--hero" role="img" aria-label="Bright living room with a sofa, potted plant and floor-to-ceiling sliding glass doors overlooking a city skyline">
      <span class="stripe stripe--blue" style="left:40px;width:22px"></span>
      <span class="stripe stripe--blue" style="left:100px;width:22px"></span>
      <span class="stripe stripe--orange" style="left:190px;width:22px"></span>
    </div>

    <div class="block" style="top:410px">
      <div class="block__head">
        <svg width="34" height="26" viewBox="0 0 34 26" aria-hidden="true"><g fill="none" stroke="var(--heading)" stroke-width="1.5"><rect x="2" y="2" width="30" height="22"/><line x1="17" y1="2" x2="17" y2="24"/><line x1="2" y1="9" x2="32" y2="9"/></g></svg>
        <h3>Our<br>Windows</h3>
      </div>
      <p>Brightpane House offers a comprehensive range of window designs, suitable for all types of buildings. All our double glazed windows offer exceptional levels of energy efficiency as well as a choice of opening styles, solid colour or wood grain effect. Whether you are looking to replace old draughty windows, transform the look of your home with a different colour or upgrade from timber windows, we will be able offer you a product which will fit your brief. All windows fitted carry a ten year insurance backed guarantee and you will be issued with a Fenstra certificate.</p>
      <p class="list">Casement, Tilt-and-Turn, Vertical slider / sash windows, Bow or bay window, French windows</p>
    </div>

    <div class="block" style="top:548px">
      <div class="block__head">
        <svg width="34" height="26" viewBox="0 0 34 26" aria-hidden="true"><g fill="none" stroke="var(--heading)" stroke-width="1.5"><rect x="4" y="2" width="16" height="22"/><circle cx="16" cy="13" r="1.4"/><rect x="22" y="9" width="8" height="7"/></g></svg>
        <h3>Our<br>Doors</h3>
      </div>
      <p>At Brightpane House we offer a comprehensive range of door options to meet your requirements. With over 190 colour options, a large selection of hardware and glass designs to compliment your new door, we are sure to meet your requirements. All of our doors are fitted with multi-point locking systems, high security cylinders and fully adjustable hinges. This means your new door will not only be extremely secure but will keep the most extreme British weather at bay.</p>
      <p class="list">Composite doors, Bi-folding doors, uPVC doors, Patio doors, French doors, Stable doors</p>
    </div>

    <div class="block" style="top:672px">
      <div class="block__head">
        <svg width="34" height="26" viewBox="0 0 34 26" aria-hidden="true"><g fill="none" stroke="var(--heading)" stroke-width="1.5"><rect x="4" y="2" width="16" height="22"/><circle cx="16" cy="13" r="1.4"/><rect x="22" y="9" width="8" height="7"/></g></svg>
        <h3>Landlord<br>Services</h3>
      </div>
      <p>Brightpane House offer a service specifically for letting agents and landlords. We assess jobs with a view to offering realistic repairs, unless repairs are not viable. Most doors and windows can be repaired, greatly reducing the cost of replacement.</p>
      <p class="list">Repairs, Replacements, Adjustments, Surveys</p>
    </div>

    <div class="footer">
      <span class="phone">
        <svg width="14" height="14" viewBox="0 0 24 24" aria-hidden="true"><path fill="#555" d="M6.6 10.8a15 15 0 0 0 6.6 6.6l2.2-2.2c.3-.3.7-.4 1-.2 1.1.4 2.3.6 3.6.6.6 0 1 .4 1 1V20c0 .6-.4 1-1 1A17 17 0 0 1 3 4c0-.6.4-1 1-1h3.5c.6 0 1 .4 1 1 0 1.3.2 2.5.6 3.6.1.3 0 .7-.2 1z"/></svg>
        01632 960 418
      </span>
      <span class="brand"><span class="brand__mark"></span>Brightpane House</span>
    </div>
  </section>
</div>
</body>
</html>
```